依頼詳細
■パッケージ等に使う基本デザインの依頼

個包装のパッケージ、箱パッケージ、しおりなどの基本デザインとして
利用します。個包装のパッケージはシールになる可能性があります。
基本デザインで結構です。以下に挙げるサイズ等にきっちり合わせて作成
いただく必要はありません。
※学生が描いたモチーフがありますので、こちらをもとに作成して
いただけると有難いです。アレンジは自由印してください。

<商品について>

ネーミングは「brume argentée 」です。
ブリュム アルジャンテ  と読みます。

※ネームもデザインアレンジいただければありがたいです。

以下の商品を想定していますが、この商品のミルクや抹茶に
左右されなくて結構です。

・ミルクティのラングドシャ (通常生地)
・岐阜県産抹茶のラングドシャ (黒の生地)

●商品サイズ 横50mm×縦50mm×厚さ8~10mm (多少、変動はあります)
●箱サイズ  類似商品の箱(添付)を参照ください。
●しおりサイズ  A6サイズ105×148mm(2つ折)想定

・20代~40代男女に訴求できるようなデザインを希望します。
・自家消費でなく、手土産を想定しています。
・どんな商品かは添付の写真を参照してください。
・店舗での販売が中心になります。
記載項目
パッケージの基本デザインは、3タイプほどの大きさで作成いただければ有難いです。実際のパッケージ、しおり、シーツ作成時に、サイズの調整を後日お願いすることにもなります。
希望イメージ
シンプル 複雑
単色 カラフル
暗い 明るい
日常 高級
遊び心 厳粛
未来的 伝統的
女性的 男性的
希望する色
茶系、黄・オレンジ系、紫系、白
納品ファイル
• 高解像度JPG (.jpg)
• イラストレーター形式 (.ai)
■ 選んだ理由

デザインがとても洗練されていて、多くの学生の投票を得ました。
ありがとうございました。

■ 提案者全員のお礼・コメント

皆様、たくさんのご提案ありがとうございました。とても質の高いデザインが集まって、驚いています。どれを選ぶか、最後の最後まで意見が割れました。それほど、甲乙つけがたいものでした。
また機会がありましたら、ご提案、よろしくお願いいたします。

```html
<!DOCTYPE html>
<html lang="ja">
<head>
<meta charset="utf-8">
<title>Brume argentée — Box Package</title>
<link rel="stylesheet" href="https://fonts.googleapis.com/css2?family=Cormorant+Garamond:wght@500&family=Noto+Serif+JP:wght@400&family=Noto+Sans+JP:wght@400&display=swap">
<style>
  :root {
    --paper: #ffffff;
    --ink: #222222;
    --sun-yellow: #f7d43c;
    --sun-amber: #f4a623;
    --sun-orange: #ef8417;
    --sun-deep: #ec7410;
    --cream: #fffbe6;
    --fold-line: rgba(255, 255, 255, 0.55);
  }
  * { margin: 0; padding: 0; box-sizing: border-box; }
  html, body { width: 682px; height: 1200px; overflow: hidden; background: var(--paper); }
  .dieline { position: relative; width: 682px; height: 1200px; }

  .spec {
    position: absolute; left: 24px; top: 22px;
    font-family: "Noto Sans JP", sans-serif; font-size: 15px; line-height: 1.45; color: var(--ink);
  }

  .panel { position: absolute; overflow: hidden; }
  .body-wrap {
    left: 0; top: 136px; width: 682px; height: 912px;
    background: linear-gradient(180deg, var(--sun-yellow) 0%, var(--sun-amber) 28%, var(--sun-orange) 60%, var(--sun-deep) 100%);
  }
  .flap-top {
    left: 216px; top: 0; width: 261px; height: 136px;
    background: linear-gradient(0deg, var(--sun-yellow) 0%, #f9e27a 100%);
  }
  .flap-bottom {
    left: 216px; top: 1048px; width: 261px; height: 152px;
    background: linear-gradient(180deg, var(--sun-orange) 0%, var(--sun-deep) 100%);
  }

  .fold { position: absolute; background: var(--fold-line); }
  .fold-v { top: 136px; width: 1px; height: 912px; }
  .fold-h { left: 0; width: 682px; height: 1px; }

  .sunburst {
    position: absolute; left: 96px; top: -90px; width: 500px; height: 420px;
    background: radial-gradient(ellipse at 50% 40%, rgba(255,255,255,0.98) 0%, rgba(255,251,225,0.85) 18%, rgba(255,240,170,0.45) 45%, rgba(255,230,140,0) 72%);
  }

  .brand {
    position: absolute; left: 0; width: 100%; text-align: center;
    font-family: "Cormorant Garamond", serif; font-weight: 500; color: var(--cream);
    white-space: nowrap;
  }
  .tagline {
    position: absolute; left: 0; width: 100%; text-align: center;
    font-family: "Cormorant Garamond", serif; font-weight: 500; color: var(--cream);
    letter-spacing: 0.12em; white-space: nowrap;
  }
  .kana {
    position: absolute; left: 0; width: 100%; text-align: center;
    font-family: "Noto Serif JP", serif; color: var(--cream); white-space: nowrap;
  }
  .mark-dot {
    position: absolute; left: 50%; border-radius: 50%;
    border: 1.5px solid var(--cream);
  }

  .front .mark-dot { top: 610px; width: 34px; height: 34px; margin-left: -17px; }
  .front .brand { top: 640px; font-size: 40px; }
  .front .kana { top: 694px; font-size: 12px; letter-spacing: 0.1em; }
  .front .tagline { top: 778px; font-size: 11px; }

  .flap-top .inverted { position: absolute; inset: 0; transform: rotate(180deg); }
  .flap-top .brand { top: 64px; font-size: 30px; color: #fff; }
  .flap-top .tagline { top: 104px; font-size: 8px; color: #fff; }

  .flap-bottom .mark-dot { top: 30px; width: 22px; height: 22px; margin-left: -11px; }
  .flap-bottom .brand { top: 50px; font-size: 30px; }
  .flap-bottom .tagline { top: 92px; font-size: 8px; }
  .flap-bottom .tagline.sub { top: 118px; font-size: 7px; }

  .side { position: absolute; top: 0; height: 912px; }
  .side-left { left: 0; width: 216px; }
  .side-right { left: 477px; width: 205px; }
  .side-text {
    position: absolute; top: 544px; white-space: nowrap;
    font-family: "Cormorant Garamond", serif; font-weight: 500; color: var(--cream);
    transform-origin: 0 0; transform: rotate(90deg);
  }
  .side-name { font-size: 38px; }
  .side-sub { font-size: 11px; letter-spacing: 0.12em; }
  .side-left .side-name { left: 118px; }
  .side-left .side-sub { left: 160px; }
  .side-right .side-name { left: 82px; }
  .side-right .side-sub { left: 124px; }
</style>
</head>
<body>
<main class="dieline">
  <p class="spec">縦 240mm<br>横 80mm<br>高さ 60mm</p>

  <section class="panel flap-top">
    <div class="inverted">
      <p class="brand">Brume argentée</p>
      <p class="tagline">LANGUE DE CHAT</p>
    </div>
  </section>

  <section class="panel body-wrap">
    <div class="sunburst" role="img" aria-label="Radiant sun glow with white lace medallion ornament"></div>

    <div class="side side-left">
      <p class="side-text side-name">Brume argentée</p>
      <p class="side-text side-sub">LANGUE DE CHAT</p>
    </div>

    <div class="front">
      <span class="mark-dot"></span>
      <p class="brand">Brume argentée</p>
      <p class="kana">ブリュム アルジャンテ</p>
      <p class="tagline">LANGUE DE CHAT</p>
    </div>

    <div class="side side-right">
      <p class="side-text side-name">Brume argentée</p>
      <p class="side-text side-sub">LANGUE DE CHAT</p>
    </div>
  </section>

  <section class="panel flap-bottom">
    <span class="mark-dot"></span>
    <p class="brand">Brume argentée</p>
    <p class="tagline">BLACK DE CHAT</p>
    <p class="tagline sub">LANGUE DE CHAT</p>
  </section>

  <span class="fold fold-v" style="left:216px"></span>
  <span class="fold fold-v" style="left:477px"></span>
  <span class="fold fold-h" style="top:136px"></span>
  <span class="fold fold-h" style="top:1048px"></span>
</main>
</body>
</html>
```